KLT Business cards

I currently have a logo that was designed by a sketch harbor designer. I would like this to be added to the business card.

We are an innovative new start-up business offering finance solutions to the car dealership market in the UK. So our clients are quiet traditional, so are cards need to fit in, but at the same time show we are a modern online business.

Industry/Entity Type

Finance

```html
<!DOCTYPE html>
<html lang="en">
<head>
<meta charset="utf-8">
<title>KLT Business Cards</title>
<link href="https://fonts.googleapis.com/css2?family=Open+Sans:wght@400;600;700&display=swap" rel="stylesheet">
<style>
  :root {
    --bg: #eceae6;
    --navy: #1f2d4e;
    --blue-deep: #3d4680;
    --blue-mid: #5a64a3;
    --blue-light: #8d96cc;
    --grey: #9a9ea6;
    --ink: #2b3550;
    --white: #ffffff;
    --faint: #eef0f3;
  }
  * { box-sizing: border-box; margin: 0; padding: 0; }
  html, body { width: 1200px; height: 784px; overflow: hidden; }
  body {
    background: var(--bg);
    font-family: "Open Sans", sans-serif;
    position: relative;
  }
  .card {
    position: absolute;
    top: 237px;
    width: 530px;
    height: 310px;
    border-radius: 4px;
    overflow: hidden;
    box-shadow: 0 6px 18px rgba(0,0,0,0.12);
  }
  /* Front */
  .card--front { left: 45px; background: var(--blue-deep); }
  .front-pattern {
    position: absolute; inset: 0;
    background:
      radial-gradient(ellipse at 80% 10%, var(--blue-light) 0%, transparent 55%),
      radial-gradient(ellipse at 10% 90%, var(--blue-mid) 0%, transparent 60%),
      linear-gradient(135deg, var(--blue-mid), var(--blue-deep));
  }
  .front-logo {
    position: absolute; left: 0; right: 0; top: 95px;
    display: flex; align-items: center; justify-content: center; gap: 16px;
    color: var(--white);
  }
  .logo-dot {
    width: 62px; height: 62px; border-radius: 50%;
    border: 5px solid currentColor;
  }
  .logo-name {
    font-weight: 600; font-size: 30px; line-height: 1.05;
  }
  .tagline {
    position: absolute; left: 0; right: 0; bottom: 62px;
    text-align: center; color: var(--white);
    font-size: 17px; letter-spacing: 9px;
  }
  /* Back */
  .card--back { left: 625px; background: var(--white); }
  .back-logo {
    position: absolute; left: 40px; top: 40px;
    display: flex; align-items: center; gap: 12px;
    color: var(--navy);
  }
  .back-logo .logo-dot { width: 54px; height: 54px; border-width: 5px; }
  .back-logo .logo-name { font-size: 24px; }
  .faint-ring {
    position: absolute; right: -40px; top: 70px;
    width: 190px; height: 190px; border-radius: 50%;
    border: 10px solid var(--faint);
  }
  .person { position: absolute; left: 40px; top: 168px; }
  .person-name { color: var(--navy); font-weight: 700; font-size: 16px; }
  .person-role { color: var(--grey); font-size: 13px; margin-top: 2px; }
  .contacts {
    position: absolute; left: 40px; top: 222px;
    list-style: none; color: var(--ink); font-size: 13px; line-height: 19px;
  }
  .contacts li { display: flex; align-items: center; gap: 6px; }
  .contacts svg { width: 13px; height: 13px; flex: none; }
</style>
</head>
<body>
  <section class="card card--front">
    <div class="front-pattern" role="img" aria-label="Decorative field of soft blue ellipses receding in perspective"></div>
    <div class="front-logo">
      <span class="logo-dot"></span>
      <span class="logo-name">Kerbline Trade<br>Finance</span>
    </div>
    <p class="tagline">Drive now, pay later</p>
  </section>

  <section class="card card--back">
    <div class="faint-ring"></div>
    <div class="back-logo">
      <span class="logo-dot"></span>
      <span class="logo-name">Kerbline Trade<br>Finance</span>
    </div>
    <div class="person">
      <p class="person-name">Oliver Hartley</p>
      <p class="person-role">Founder</p>
    </div>
    <ul class="contacts">
      <li>
        <svg viewBox="0 0 16 16" fill="#6b7180"><path d="M3 1l3 3-1.5 2c1 2 3 4 5 5L11.5 9.5l3 3-2 2.5C6 14 2 10 1 3z"/></svg>
        07700 900418
      </li>
      <li>
        <svg viewBox="0 0 16 16"><circle cx="8" cy="8" r="7" fill="#6b7180"/></svg>
        oliver.hartley_klt
      </li>
      <li>
        <svg viewBox="0 0 16 16" fill="none" stroke="#6b7180" stroke-width="1.4"><circle cx="8" cy="8" r="6.5"/><ellipse cx="8" cy="8" rx="3" ry="6.5"/><path d="M1.5 8h13M2.5 4.5h11M2.5 11.5h11"/></svg>
        www.kerblinefinance.com
      </li>
      <li>
        <svg viewBox="0 0 16 16" fill="none" stroke="#6b7180" stroke-width="1.4"><rect x="1.5" y="3.5" width="13" height="9" rx="1"/><path d="M1.5 4l6.5 5 6.5-5"/></svg>
        oliver.hartley@kerblinefinance.com
      </li>
    </ul>
  </section>
</body>
</html>
```